Business Card Design Project

We are looking for a new business card design to go with our new logo. We need to have a front and back card with our name and numberous phone numbers on the front and our addresses on the back. We will need to be able to edit the cards to have different names and numbers. Right now our card looks too busy and cluttered. We need to have our Brightmere Estates Collective Logo Prominently displayed. We will also need the Havlin Sorrento Realty Midtown, the relator logo and the equal housing logo on the front somewhere. We would like to have our addresses on the back along with the quote "Our most important goal is to exceed the expectations of our clients and the finest compliment we can received is a referral from a friend or past client. Thank you for your support!" Also, we would like the "Please follow us on : zolvanet logo, krambo loto, felquara logo and tindlebarn logo" I've attached our new logo and what our current business card looks like.
Business

```html
<!DOCTYPE html>
<html lang="en">
<head>
<meta charset="utf-8">
<title>Brightmere Estates Collective – Business Card</title>
<link href="https://fonts.googleapis.com/css2?family=Sorts+Mill+Goudy:ital@0;1&family=Crimson+Text:ital@0;1&display=swap" rel="stylesheet">
<style>
  :root{
    --backdrop:#d38a3e;
    --paper:#ffffff;
    --brand-red:#b5262e;
    --band-red:#c0313a;
    --band-dark:#3a3a3c;
    --ink:#1e1e1e;
    --logo-soft:#d9a3a3;
    --back-top:#d22b30;
    --back-bottom:#8f1d22;
    --quote-band:rgba(236,170,170,.78);
    --tab:rgba(70,30,30,.72);
    --white:#ffffff;
  }
  *{margin:0;padding:0;box-sizing:border-box}
  html,body{width:1200px;height:900px;overflow:hidden}
  body{background:var(--backdrop);position:relative;font-family:"Sorts Mill Goudy",Georgia,serif;color:var(--ink)}

  /* Front */
  .card-front{position:absolute;left:13px;top:12px;width:657px;height:406px;background:var(--paper);overflow:hidden}
  .brand-front{position:absolute;left:45px;top:70px;width:240px;text-align:center;font-size:30px;line-height:1.1;color:var(--logo-soft)}
  .agent-name{position:absolute;left:55px;top:214px;font-size:26px;color:var(--brand-red)}
  .agent-title{position:absolute;left:82px;top:243px;font-family:"Crimson Text",Georgia,serif;font-style:italic;font-size:13px}
  .agent-email{position:absolute;left:55px;top:285px;font-size:17px}
  .agent-email span{color:var(--brand-red)}
  .phones{position:absolute;left:348px;top:222px;font-size:17px;line-height:25px;border-collapse:collapse}
  .phones td{padding:0}
  .phones .label{color:var(--brand-red);width:92px}
  .phones .num{letter-spacing:1px}
  .footer-band{position:absolute;left:0;top:354px;width:100%;height:32px;background:var(--band-red)}
  .footer-strip{position:absolute;left:0;top:386px;width:100%;height:20px;background:var(--band-dark)}
  .broker-badge{position:absolute;left:75px;top:5px;width:94px;height:22px;background:var(--paper);font-size:7px;line-height:10px;color:var(--brand-red);text-align:center;padding-top:1px}
  .plain-badge{position:absolute;top:5px;width:22px;height:22px;background:var(--paper);border:2px solid var(--ink)}
  .site{position:absolute;left:348px;top:7px;font-size:17px;letter-spacing:1px;color:var(--ink)}
  .site span{color:var(--paper)}

  /* Back */
  .card-back{position:absolute;left:533px;top:484px;width:657px;height:406px;background:linear-gradient(var(--back-top) 0 128px,var(--back-bottom) 209px);overflow:hidden}
  .address-tab{position:absolute;left:241px;top:0;width:173px;height:82px;background:var(--tab);border:1px solid rgba(255,255,255,.5);border-top:none;border-radius:0 0 6px 6px;color:var(--white);text-align:center;font-size:15px;line-height:18px;padding-top:24px}
  .quote-band{position:absolute;left:0;top:128px;width:100%;height:81px;background:var(--quote-band);font-family:"Crimson Text",Georgia,serif;font-style:italic;font-size:17px;line-height:21px;text-align:center;padding:9px 20px 0;color:#2a1414}
  .social{position:absolute;left:47px;top:261px;display:flex;gap:16px}
  .social-chip{width:60px;height:60px;border-radius:8px;background:rgba(255,255,255,.14);border:1px solid rgba(255,255,255,.35);color:var(--white);font-size:11px;display:flex;align-items:center;justify-content:center;text-align:center}
  .follow-tab{position:absolute;left:109px;top:349px;width:166px;height:60px;background:rgba(40,10,10,.7);border:1px solid rgba(255,255,255,.45);border-radius:6px 6px 0 0;color:var(--white);font-family:"Crimson Text",Georgia,serif;font-style:italic;font-size:16px;text-align:center;padding-top:8px}
  .brand-back{position:absolute;left:368px;top:270px;width:240px;text-align:center;font-size:30px;line-height:1.1;color:var(--white)}
</style>
</head>
<body>

<section class="card-front" aria-label="Business card front">
  <div class="brand-front">Brightmere Estates Collective</div>
  <div class="agent-name">Clara Vennholt</div>
  <div class="agent-title">Broker, Listing Specialist</div>
  <div class="agent-email"><span>clara</span>@brightmere.com</div>
  <table class="phones">
    <tr><td class="label">Cell</td><td class="num">(555) 214-7390</td></tr>
    <tr><td class="label">Office</td><td class="num">(555) 386-0142</td></tr>
    <tr><td class="label">Toll Free</td><td class="num">(800) 555-0178</td></tr>
    <tr><td class="label">Fax</td><td class="num">(555) 472-9015</td></tr>
  </table>
  <div class="footer-band">
    <div class="broker-badge">Havlin Sorrento Realty Midtown</div>
    <div class="plain-badge" style="left:173px"></div>
    <div class="plain-badge" style="left:200px"></div>
    <div class="site">www.<span>BrightmereEstates</span>.com</div>
  </div>
  <div class="footer-strip"></div>
</section>

<section class="card-back" aria-label="Business card back">
  <div class="address-tab">418 Harborview Plaza<br>7200 NW Alder Ct, #310<br>Ashford, OR 97000</div>
  <p class="quote-band">Our most important goal is to exceed the expectations of our clients and the finest compliment we can receive is a referral from a friend or past client. Thank you for your support!</p>
  <div class="social">
    <div class="social-chip">zolvanet</div>
    <div class="social-chip">krambo</div>
    <div class="social-chip">felquara</div>
    <div class="social-chip">tindlebarn</div>
  </div>
  <div class="follow-tab">Please follow us on</div>
  <div class="brand-back">Brightmere Estates Collective</div>
</section>

</body>
</html>
```